Copper Fern Photography

Internet sales of landscape photography
Some background on the name.... I'm originally from Kentucky hence the "Copper" and I now live in California wine country, hence the "Fern." The blue coloring in the name is from the Harlow Falcons and the name "photography" is done in a bourbon lettering font. Hope this helps.
Updates
Please include email as dennis@copperfernphotography.com
Please make website www.copperfernphotography.com and ad QR code if possible.
Industry/Entity Type
Landscape
Contact Information for Business Card
Dennis Marlowe
www.copperfernphoto.com
707-555-0192
Requirements
Must have
- My design logo, all contact info :)
I like the thought of a QR Code along with the written link also.

```html
<!DOCTYPE html>
<html lang="en">
<head>
<meta charset="utf-8">
<title>Copper Fern Photography – Business Card</title>
<link rel="stylesheet" href="https://fonts.googleapis.com/css2?family=Quicksand:wght@500;600;700&display=swap">
<style>
  :root {
    --backdrop: #666666;
    --card-white: #ffffff;
    --brand-blue: #1560ac;
    --ornament-blue: #8aa3d8;
    --text-light: #ffffff;
  }
  * { margin: 0; padding: 0; box-sizing: border-box; }
  html, body {
    width: 1200px;
    height: 1000px;
    overflow: hidden;
    background: var(--backdrop);
  }
  .business-card {
    position: absolute;
    left: 150px;
    top: 236px;
    width: 900px;
    height: 528px;
    background: var(--card-white);
    font-family: "Quicksand", sans-serif;
    overflow: hidden;
  }
  .brand-area {
    position: absolute;
    left: 0; top: 0;
    width: 900px; height: 313px;
    display: flex;
    flex-direction: column;
    align-items: center;
    justify-content: center;
    color: var(--brand-blue);
    font-weight: 700;
    padding-top: 10px;
  }
  .brand-name {
    font-size: 76px;
    line-height: 1;
  }
  .brand-tagline {
    font-size: 40px;
    letter-spacing: 10px;
    line-height: 1;
    margin-top: 14px;
  }
  .contact-band {
    position: absolute;
    left: 0; top: 313px;
    width: 900px; height: 215px;
    background: var(--brand-blue);
    color: var(--text-light);
  }
  .ornament {
    position: absolute;
    background: var(--ornament-blue);
    opacity: 0.55;
  }
  .ornament--lower-left { left: 0; top: 98px; width: 137px; height: 117px; border-radius: 0 40px 0 0; }
  .ornament--upper-right { right: 0; top: 7px; width: 118px; height: 130px; border-radius: 40px 0 0 40px; }
  .holder-name {
    position: absolute;
    left: 169px; top: 24px;
    font-size: 40px;
    font-weight: 600;
    letter-spacing: 1px;
    line-height: 1.1;
  }
  .contact-line {
    position: absolute;
    left: 339px;
    display: flex;
    align-items: center;
    gap: 12px;
    font-size: 24px;
    font-weight: 500;
    line-height: 1.2;
  }
  .contact-line--phone { top: 86px; }
  .contact-line--email { top: 122px; }
  .contact-line--web { top: 158px; }
  .contact-icon { width: 22px; height: 22px; flex: none; }
  .qr-code {
    position: absolute;
    left: 806px; top: 142px;
    width: 62px; height: 62px;
    background: var(--card-white);
    border-radius: 4px;
  }
</style>
</head>
<body>
  <div class="business-card">
    <header class="brand-area">
      <div class="brand-name">Copper Fern</div>
      <div class="brand-tagline">PHOTOGRAPHY</div>
    </header>

    <section class="contact-band">
      <div class="ornament ornament--lower-left" role="img" aria-label="Faint decorative leaf ornament"></div>
      <div class="ornament ornament--upper-right" role="img" aria-label="Faint decorative leaf ornament"></div>

      <div class="holder-name">Dennis Marlowe</div>

      <div class="contact-line contact-line--phone">
        <svg class="contact-icon" viewBox="0 0 22 22" aria-hidden="true">
          <rect x="0" y="0" width="22" height="22" rx="4" fill="#ffffff"/>
          <path d="M7 4.5 L9.5 4.5 L10.5 8 L8.8 9.3 C9.6 11.2 10.8 12.4 12.7 13.2 L14 11.5 L17.5 12.5 L17.5 15 C17.5 16.2 16.5 17.3 15 17.2 C9.5 16.6 5.4 12.5 4.8 7 C4.7 5.5 5.8 4.5 7 4.5 Z" fill="#1560ac"/>
        </svg>
        <span>707-555-0192</span>
      </div>

      <div class="contact-line contact-line--email">
        <svg class="contact-icon" viewBox="0 0 22 22" aria-hidden="true">
          <rect x="0" y="0" width="22" height="22" rx="4" fill="#ffffff"/>
          <g fill="none" stroke="#1560ac" stroke-width="1.4">
            <rect x="4" y="6" width="14" height="10" rx="1"/>
            <polyline points="4,6.5 11,12 18,6.5"/>
          </g>
        </svg>
        <span>dennis@copperfernphotography.com</span>
      </div>

      <div class="contact-line contact-line--web">
        <svg class="contact-icon" viewBox="0 0 22 22" aria-hidden="true">
          <rect x="0" y="0" width="22" height="22" rx="4" fill="#ffffff"/>
          <g fill="none" stroke="#1560ac" stroke-width="1.4">
            <circle cx="11" cy="11" r="6.5"/>
            <ellipse cx="11" cy="11" rx="3" ry="6.5"/>
            <line x1="4.5" y1="11" x2="17.5" y2="11"/>
          </g>
        </svg>
        <span>www.copperfernphotography.com</span>
      </div>

      <div class="qr-code" role="img" aria-label="QR code linking to the website"></div>
    </section>
  </div>
</body>
</html>
```